Website Design : Design the digital space for the UK’s coolest offline movement – Pebblestone June

Think 1990s throwback meets modern minimalism—analogue culture brought into the now. The site should evoke a sense of a cool, fun rebellion. It should feel like an intentional lifestyle movement, not a corporate campaign.

Task Description:
We’re looking for a creative website designer to build a visually engaging, easy-to-navigate website for Pebblestone June CIC, a new UK-based social impact initiative encouraging individuals and families to reduce smartphone and social media use during April each year.
The site must be fully WIX-compatible, mobile-responsive, and built with accessibility, clarity, and inspiration in mind. The tone is bold but friendly—similar to Hatchwick UK—with clear calls to action, high readability, and a confident identity. It should feel like a positive challenge, not a guilt trip.

See Website Design Brief attached.
See Website Content (written content for the website) attached.
Draft logo included in attachments.
Updates

While 'Analogue' may invoke a sepia coloured world, we want this to website to be cool : vibrant, bold, energetic and expressive. Maybe even a little rebellious! It should be highly visual and communicate the energy and enthusiasm behind the 'analogue movement'! Possibly look at featuring a layered mix of saturated colours, playful typography, and a dynamic, urban edge.

Maybe look at using a vivid mix of neon tones contrasted with darker outlines and shadowing to make elements pop. Graffiti even? Graffiti wall textures, paint splatters, brick walls, and spray can motifs can be used subtly as background layers. Urban environments, street scenes, murals, community gatherings, and artistic expression.

We appreciate the target audience is rather wide, and understand its a big ask to appeal to such a wide group - Parents and Families (Ages 30–50), Professionals and Conscious Consumers (Ages 25–45), Teenagers and Young Adults (Ages 13–25), Schools and Educators, Mental Health Advocates, Researchers, and Funders.

Food for thought:
https://brevlink.example/d/qTzW8kP

Target Market(s)

Parents and Families (Aged 30–50), Professionals and Conscious Consumers (Aged 25–45), Teenagers & Young Adults (Aged 13–25), Schools & Educators, Funders, Supporters & Partners

Industry/Entity Type

Digital Wellbeing and Behavioural Health Campaigning, Public Mental Health and Lifestyle Awareness, Technology & Wellbeing Education (Nonprofit Sector)

Font styles to use
Other font styles liked:
• • Primary Font: Old-school typewriter-style serif font for headers (e.g. "Courier New", "American Typewriter", or retro fonts like "IBM Plex Mono") • Body Font: Clean, modern sans-serif (e.g. "Inter", "Lato", or "Raleway") for readability

```html
<!DOCTYPE html>
<html lang="en">
<head>
<meta charset="utf-8">
<title>Pebblestone June – Blogs &amp; Publications</title>
<link rel="stylesheet" href="https://fonts.googleapis.com/css2?family=Courier+Prime&family=IBM+Plex+Mono:wght@400;500;600&family=Montserrat:wght@400&display=swap">
<style>
:root{
  --cyan:#00f0ff;
  --ink:#111111;
  --grey:#5a5a5a;
  --line:#dcdcdc;
  --card-border:#e2e2e2;
  --night:#0b0014;
  --white:#ffffff;
  --pattern:#ececec;
}
*{box-sizing:border-box;margin:0;padding:0}
html,body{width:1200px;height:3009px;overflow:hidden;background:var(--white)}
body{position:relative;font-family:"IBM Plex Mono",monospace;color:var(--ink)}
a{color:inherit;text-decoration:none}

/* header */
.site-header{position:absolute;left:0;top:0;width:1200px;height:110px;border-bottom:1px solid var(--line)}
.brand{position:absolute;display:flex;align-items:center;gap:18px}
.brand-mark{width:72px;height:72px;border:4px solid currentColor;border-radius:50%}
.brand-name{font-family:"Courier Prime",monospace;font-size:34px;letter-spacing:1px;line-height:1}
.brand-tag{font-family:"Montserrat",sans-serif;font-size:14px;margin-top:8px}
.site-header .brand{left:144px;top:18px;color:var(--ink)}
.auth{position:absolute;top:26px;left:657px;display:flex;gap:12px}
.auth a{width:124px;height:43px;display:flex;align-items:center;justify-content:center;font-size:14px;font-weight:500;border:2px solid var(--ink)}
.auth .btn-login{background:var(--cyan);border-color:var(--cyan)}

.main-nav{position:absolute;top:110px;left:0;width:1200px;height:47px;border-bottom:1px solid var(--line)}
.main-nav a{position:absolute;top:0;height:47px;line-height:47px;font-size:15px;font-weight:500;letter-spacing:.5px}
.main-nav a.active{border-bottom:2px solid var(--ink)}

/* title */
.page-title{position:absolute;top:220px;left:0;width:1200px;text-align:center;font-size:58px;font-weight:500;letter-spacing:3px;line-height:1}
.pattern-strip{position:absolute;left:0;width:1200px;height:14px;background:var(--pattern)}

/* decorations */
.deco{position:absolute;background:linear-gradient(135deg,#f4f4f4,#e6e6e6)}

/* tabs */
.tabs{position:absolute;top:436px;left:186px;width:828px;height:52px;display:flex;border:1px solid var(--cyan)}
.tabs a{flex:1;display:flex;align-items:center;justify-content:center;font-size:25px;font-weight:500;letter-spacing:1px}
.tabs .active{background:var(--cyan)}

/* cards */
.feed{position:absolute;top:541px;left:141px;width:916px;display:flex;flex-direction:column;gap:15px}
.card{height:314px;border:2px solid var(--card-border);display:flex;padding:48px 43px 0 43px;gap:38px}
.card-meta{width:350px;flex:none}
.card-title{font-family:"Courier Prime",monospace;font-size:18px;line-height:26px;font-weight:400;letter-spacing:.3px}
.card-source{display:block;margin-top:20px;font-size:14px;line-height:29px;color:var(--grey);text-decoration:underline;text-underline-offset:4px}
.card-body{width:442px}
.card-body p{font-size:14px;line-height:28.6px;color:var(--grey);text-align:justify;height:172px;overflow:hidden;margin-top:-8px}
.btn-read{display:inline-flex;align-items:center;justify-content:center;width:115px;height:41px;margin-top:17px;background:var(--cyan);font-size:13.5px;font-weight:500}

/* footer */
.site-footer{position:absolute;top:2599px;left:0;width:1200px;height:410px;background:var(--night);color:var(--white)}
.site-footer .brand{left:369px;top:74px}
.footer-nav a{position:absolute;top:196px;font-size:15px;font-weight:600;letter-spacing:.5px}
.legal{position:absolute;top:244px;width:1200px;text-align:center;font-size:15.5px;letter-spacing:.5px}
.legal span{margin:0 18px}
.social{position:absolute;top:310px;left:502px;display:flex;gap:9px}
.social a{width:32px;height:32px;border-radius:50%;background:var(--white)}
</style>
</head>
<body>

<header class="site-header">
  <a class="brand" href="#">
    <span class="brand-mark"></span>
    <span>
      <span class="brand-name">Pebblestone June</span>
      <span class="brand-tag" style="display:block">Go Pebblestone for June</span>
    </span>
  </a>
  <div class="auth">
    <a class="btn-login" href="#">LOGIN</a>
    <a href="#">REGISTER</a>
    <a href="#">DONATE</a>
  </div>
</header>

<nav class="main-nav">
  <a href="#" style="left:194px">SUPPORT US</a>
  <a href="#" style="left:359px">ABOUT US</a>
  <a href="#" style="left:503px">SMARTPHONE HEALTH</a>
  <a href="#" style="left:732px">DIGITAL CHALLENGES</a>
  <a href="#" class="active" style="left:969px">BLOG</a>
</nav>

<h1 class="page-title">BLOGS &amp; PUBLICATIONS</h1>
<div class="pattern-strip" style="top:342px" role="img" aria-label="Decorative band of small geometric shapes"></div>

<div class="deco" style="left:1093px;top:437px;width:107px;height:129px" role="img" aria-label="Decorative concentric line arcs"></div>
<div class="deco" style="left:0;top:603px;width:85px;height:107px" role="img" aria-label="Decorative wavy line pattern"></div>
<div class="deco" style="left:1120px;top:2404px;width:80px;height:128px" role="img" aria-label="Decorative concentric line arcs"></div>

<div class="tabs">
  <a href="#">BLOGS</a>
  <a href="#" class="active">PUBLICATIONS &amp; ARTICLES</a>
</div>

<main class="feed">
  <article class="card">
    <div class="card-meta">
      <h2 class="card-title">Brightwave Launches Age Guidance For Smartphone Usage In Drive To Improve Children’s Digital Awareness</h2>
      <a class="card-source" href="#">Brightwave Online Newsroom, 25 August 24</a>
    </div>
    <div class="card-body">
      <p>Brightwave is taking a significant step to safeguard children in the digital world by introducing age-specific guidance for smartphone usage. The initiative comes in response to growing concerns among parents about screen time, online safety, and how digital device usage can affect child wellbeing.</p>
      <a class="btn-read" href="#">READ MORE</a>
    </div>
  </article>

  <article class="card">
    <div class="card-meta">
      <h2 class="card-title">Is there a middle way on children and smartphones? This researcher thinks so</h2>
      <a class="card-source" href="#">Ledger Weekly – Harold Vance<br>12 May 24</a>
    </div>
    <div class="card-body">
      <p style="text-align:left">Try unlimited access<br>Only Rs100 for 4 weeks<br>Then Rs4335 per month.<br>Complete digital access to quality LW journalism on any device.<br>Cancel anytime during your trial.</p>
      <a class="btn-read" href="#">READ MORE</a>
    </div>
  </article>

  <article class="card">
    <div class="card-meta">
      <h2 class="card-title">KA study: Over a third of UK consumers keen on a New Year "digital detox"</h2>
      <a class="card-source" href="#" style="margin-top:46px">KA Study, Colin Brayfield, 10 Jan 25</a>
    </div>
    <div class="card-body">
      <p>38% of UK consumers are concerned about having too much screen time and are keen to have a “digital detox”Almost half (47%) of 18-34 year olds view their online activities as more disruptive than beneficial to their well-being67% of households believe that government and regulators aren’t doing enough to</p>
      <a class="btn-read" href="#">READ MORE</a>
    </div>
  </article>

  <article class="card">
    <div class="card-meta">
      <h2 class="card-title">Age Appropriate Design: Assessment of Clipwave, Streamly, and Vidnest Kids</h2>
      <a class="card-source" href="#">School of Computing University of Harrowfield, UK, Verity N. L. Franklin, Jenna A. Arlow and Omar Kestel – 4 Aug 22</a>
    </div>
    <div class="card-body">
      <p>Children (defined by the Data Standards Office – DSO, UK) as “a person under the age of 18 years” [12, Page 89]) are increasingly relying on online services for entertainment (e.g. to play games, to consume multimedia), for education (e.g. to support schoolwork, to learn skills),</p>
      <a class="btn-read" href="#">READ MORE</a>
    </div>
  </article>

  <article class="card">
    <div class="card-meta">
      <h2 class="card-title">Understanding Engagement With Platform Safety Technology For Reducing Exposure To Online Harms</h2>
      <a class="card-source" href="#">Public Policy Programme, The Ada Lomax Institute and Oxbury Internet Institute, University of Oxbury - Jonah Brightwell, Fiona E. Enderby, Hazel Z. Marlowe, Pia Jansen, Frances Stellan – 3 Jan 24</a>
    </div>
    <div class="card-body">
      <p>The potential for users of social media platforms to be exposed to harmful content remains a cause for concern. Numerous online harms, understood as harmful content or activity that is experienced online such as cyberstalking and hate speech (see National Government, 2019) take place everyday.</p>
      <a class="btn-read" href="#">READ MORE</a>
    </div>
  </article>

  <article class="card">
    <div class="card-meta">
      <h2 class="card-title">We wanted to change the norm on smartphone use’: grassroots campaigners on a phone-free childhood’</h2>
      <a class="card-source" href="#">The Daily Courier – Alex Morland,<br>30 Jun 24</a>
    </div>
    <div class="card-body">
      <p>Last year, Della Greenway and Clara Fernley, longtime friends who have eight- and nine-year-old daughters, began having drawn-out conversations about smartphones. Rumours were swirling that children in their daughters’ classes were asking for their own and both Greenway and Fernley</p>
      <a class="btn-read" href="#">READ MORE</a>
    </div>
  </article>
</main>

<div class="pattern-strip" style="top:2583px" role="img" aria-label="Decorative band of small geometric shapes"></div>

<footer class="site-footer">
  <a class="brand" href="#">
    <span class="brand-mark"></span>
    <span>
      <span class="brand-name">Pebblestone June</span>
      <span class="brand-tag" style="display:block">Go Pebblestone for June</span>
    </span>
  </a>
  <nav class="footer-nav">
    <a href="#" style="left:194px">SUPPORT US</a>
    <a href="#" style="left:359px">ABOUT US</a>
    <a href="#" style="left:503px">SMARTPHONE HEALTH</a>
    <a href="#" style="left:732px">DIGITAL CHALLENGES</a>
    <a href="#" style="left:969px">BLOG</a>
  </nav>
  <p class="legal">© 2025 Companyname.All Rights Reserved<span>|</span>Privacy Policy<span>|</span>Terms of Use</p>
  <div class="social">
    <a href="#" aria-label="Social channel 1"></a>
    <a href="#" aria-label="Social channel 2"></a>
    <a href="#" aria-label="Social channel 3"></a>
    <a href="#" aria-label="Social channel 4"></a>
    <a href="#" aria-label="Social channel 5"></a>
  </div>
</footer>

</body>
</html>
```